Lens Deal Scout

This website is a price comparison site specialising in Digital Photographic equipment - DSLR Cameras & Lenses etc. It is going to operate along the lines of a site called www.shutterquoteroom.com
It must look much more professional and less home made than the afforementioned site. My site will be a direct competitor to shutterquoteroom, so it must look and operate much better.
The new site is first and foremost a price information site - it is not selling anything! The message it should send to visitors is one of impartiality and unbiased information, the shops it links to are the ones who will be selling products. People who visit this site, have already decided which product they are going to buy, they are now at the stage of looking for which shop is offering the best deal based on PRICE. This is NOT a "WHAT CAMERA" site. This site is comparing DIFFERENT PRICES for the same product offered by a list of SHOPS. The site should look expensive. I have a couple of Logos which you can look at for colour ideas. I like Blue, Silver, aluminium, stainless steel, White, Grey and Black. There must be lots of product category buttons to chose from. If you can come up with anything imaginative, I will appreciate any clever ideas. Some flash technology might be nice or something visually interesting happening to catch the visitors attention. There are lots of stock photos available on the net of the kind of products we will be dealing with. In particular VELMIRA and TORQUA Digital SLR Cameras and Lenses. All the other brands are definately second division. There will be no telephone number on the page. My Logo will be at the top of the page. I have uploaded two logos for you to take your pick and a very nice picture of a very expensivr DSLR camera which you might want to utilize.
Updates

Target Market(s)

Buyers of DSLR Camera equipment 70% Male, Age group 35 to 70. The products being compared on this site are all high ticket items. Customers are usually quite well off.

Industry/Entity Type

Camera

Requirements
Must have
• Must be simple and easy to navigate to find the desired product very easily.
Nice to have
• Should have a space on the front page for "TODAYS PRICE DROPS"

```html
<!DOCTYPE html>
<html lang="en">
<head>
<meta charset="utf-8">
<title>Lens Deal Scout</title>
<link rel="stylesheet" href="https://fonts.googleapis.com/css2?family=Ubuntu:wght@300;400&display=swap">
<style>
:root{
  --page:#ffffff;
  --ink:#222222;
  --muted:#a6a6a6;
  --blue:#2aa0d8;
  --btn:#27a6e1;
  --card:#f7f7f7;
  --card-edge:#dddddd;
  --side-top:#f4f4f4;
  --side-bot:#dedede;
  --sub-line:#e6e6e6;
  --footer:#e3e3e3;
  --footer-ink:#9a9a9a;
  --photo-a:#f4f4f4;
  --photo-b:#3a3a3a;
}
*{box-sizing:border-box;margin:0;padding:0}
html,body{width:1200px;height:901px;overflow:hidden;background:var(--page)}
body{position:relative;font-family:"Ubuntu",Tahoma,sans-serif;color:var(--ink);font-size:13px}
/* sidebar */
.sidebar{position:absolute;left:57px;top:-10px;width:250px}
.sub-item{height:39.5px;line-height:39.5px;padding-left:49px;font-size:15px;border-bottom:1px solid var(--sub-line);background:#fff}
.sub-item.parent{padding-left:30px}
.sub-item.child{padding-left:49px}
.brand{height:39.5px;line-height:38px;padding-left:10px;font-size:15px;background:linear-gradient(var(--side-top),var(--side-bot));border-bottom:1px solid #fff}
.brand:last-child{border-radius:0 0 4px 4px}
.brand .count{color:var(--muted)}
/* cards */
.card{position:absolute;width:237px;background:var(--card);border:1px solid var(--card-edge);border-radius:3px;box-shadow:0 1px 3px rgba(0,0,0,.12);padding:0 9px}
.card .excerpt{font-size:13px;line-height:20px}
.card .crumbs{font-size:10px;color:var(--muted);margin-top:8px;height:17px}
.card .photo{height:158px;border:2px dashed #e2e2e2;background:radial-gradient(ellipse at 50% 55%,var(--photo-b) 0 28%,var(--photo-a) 45%);margin-bottom:9px}
.card .title{color:var(--blue);font-size:15px;line-height:20px;margin-bottom:7px}
.card .actions{position:absolute;left:9px;right:13px;bottom:9px;display:flex;justify-content:space-between;align-items:center}
.btn{background:var(--btn);color:#fff;font-size:11px;border-radius:3px;padding:0 5px;height:23px;line-height:23px}
.more{color:var(--blue);font-size:11px;display:flex;align-items:center;gap:3px}
.more svg{display:block}
/* sections */
.section-head{position:absolute;display:flex;align-items:center;gap:9px;color:var(--blue);font-size:26px;font-weight:300}
.news-item{position:absolute;left:340px;width:370px;height:66px}
.thumb{position:absolute;left:0;top:0;width:66px;height:66px;border:2px dashed #e2e2e2;background:radial-gradient(ellipse at 50% 55%,var(--photo-b) 0 26%,var(--photo-a) 42%)}
.news-item .title{position:absolute;left:80px;top:0;color:var(--blue);font-size:15px}
.news-item .lede{position:absolute;left:80px;top:26px;font-size:13px;white-space:nowrap}
.news-item .date{position:absolute;left:80px;top:47px;font-size:12px;color:var(--muted)}
.black-list{position:absolute;left:733px;top:590px;list-style:none;width:370px}
.black-list li{height:46px}
.black-list .name{font-size:15px;display:block}
.black-list .note{font-size:12px;color:var(--muted);display:block;margin-top:1px;white-space:nowrap}
.footer{position:absolute;left:0;top:846px;width:1200px;height:55px;background:var(--footer);color:var(--footer-ink);font-size:12px;padding:16px 0 0 58px}
</style>
</head>
<body>

<nav class="sidebar">
  <div class="sub-item parent">Camcorders</div>
  <div class="sub-item child">Category 5</div>
  <div class="sub-item child">Category 6</div>
  <div class="sub-item child">Category 7</div>
  <div class="sub-item child">Category 8</div>
  <div class="brand">Orvanta <span class="count">(268)</span></div>
  <div class="brand">Selkor <span class="count">(203)</span></div>
  <div class="brand">Bendra <span class="count">(162)</span></div>
  <div class="brand">Parovic <span class="count">(126)</span></div>
  <div class="brand">Kelvo <span class="count">(86)</span></div>
  <div class="brand">Medrix <span class="count">(40)</span></div>
  <div class="brand">Pentora <span class="count">(32)</span></div>
  <div class="brand">Praxilo <span class="count">(23)</span></div>
  <div class="brand">Calvo <span class="count">(15)</span></div>
  <div class="brand">Polaryn <span class="count">(14)</span></div>
  <div class="brand">Hextal <span class="count">(14)</span></div>
  <div class="brand">Aceva <span class="count">(9)</span></div>
  <div class="brand">Minora <span class="count">(6)</span></div>
  <div class="brand">Rikano <span class="count">(4)</span></div>
  <div class="brand">Premora <span class="count">(3)</span></div>
  <div class="brand">Lumira <span class="count">(2)</span></div>
</nav>

<!-- upper product row (continues above the fold) -->
<article class="card" style="left:331px;top:-40px;height:124px">
  <p class="excerpt" style="margin-top:38px">pulvinar in.</p>
  <div class="actions"><span class="btn">Add to compare</span><span class="more">more <svg width="9" height="9"><rect width="9" height="9" fill="#27a6e1"/><path d="M2 3l2.5 3L7 3" stroke="#fff" fill="none" stroke-width="1.3"/></svg></span></div>
</article>
<article class="card" style="left:594px;top:-40px;height:124px">
  <p class="excerpt" style="margin-top:38px">mattis. Aenean et velit at erat<br>faucibus luctus in quis ligula ...</p>
  <div class="actions"><span class="btn">Add to compare</span><span class="more">more <svg width="9" height="9"><rect width="9" height="9" fill="#27a6e1"/><path d="M2 3l2.5 3L7 3" stroke="#fff" fill="none" stroke-width="1.3"/></svg></span></div>
</article>
<article class="card" style="left:857px;top:-40px;height:124px">
  <p class="excerpt" style="margin-top:38px">ligula pulvinar in. Etiam eu auctor<br>diam.</p>
  <div class="actions"><span class="btn">Add to compare</span><span class="more">more <svg width="9" height="9"><rect width="9" height="9" fill="#27a6e1"/><path d="M2 3l2.5 3L7 3" stroke="#fff" fill="none" stroke-width="1.3"/></svg></span></div>
</article>

<!-- product row -->
<article class="card" style="left:331px;top:110px;height:369px">
  <p class="crumbs">Orvanta &gt; Camcorers &gt; Dolor</p>
  <div class="photo" role="img" aria-label="Product photo of a black DSLR camera with lens"></div>
  <h3 class="title" style="font-weight:400">Vestibulum ut purus in lorem cursus auctor eu ut lacus.</h3>
  <p class="excerpt">Lacus, et ultricies metus tempor quis. Mauris lacinia tristique tellus a mattis. Aenean et velit at erat faucibus luctus in quis ligula ...</p>
  <div class="actions"><span class="btn">Add to compare</span><span class="more">more <svg width="9" height="9"><rect width="9" height="9" fill="#27a6e1"/><path d="M2 3l2.5 3L7 3" stroke="#fff" fill="none" stroke-width="1.3"/></svg></span></div>
</article>
<article class="card" style="left:594px;top:110px;height:369px">
  <p class="crumbs">Sovelo &gt; Photography &gt; Lorem</p>
  <div class="photo" role="img" aria-label="Product photo of a black DSLR camera with lens"></div>
  <h3 class="title" style="font-weight:400">Nullam pulvinar auctor massa.</h3>
  <p class="excerpt">Lacus, et ultricies metus tempor quis. Mauris lacinia tristique tellus a mattis. Aenean et velit at erat faucibus luctus in quis ligula cursus dictum arcu, vel porta ligula ...</p>
  <div class="actions"><span class="btn">Add to compare</span><span class="more">more <svg width="9" height="9"><rect width="9" height="9" fill="#27a6e1"/><path d="M2 3l2.5 3L7 3" stroke="#fff" fill="none" stroke-width="1.3"/></svg></span></div>
</article>
<article class="card" style="left:857px;top:110px;height:369px">
  <p class="crumbs">Sovelo &gt; Photography &gt; Lorem</p>
  <div class="photo" role="img" aria-label="Product photo of a black DSLR camera with lens"></div>
  <h3 class="title" style="font-weight:400">Donec et lorem id ipsum sodales gravida. Pellentesque imperdiet.</h3>
  <p class="excerpt">Lacus, et ultricies metus tempor quis. Mauris lacinia tristique tellus a mattis. Aenean et velit at&nbsp; ...</p>
  <div class="actions"><span class="btn">Add to compare</span><span class="more">more <svg width="9" height="9"><rect width="9" height="9" fill="#27a6e1"/><path d="M2 3l2.5 3L7 3" stroke="#fff" fill="none" stroke-width="1.3"/></svg></span></div>
</article>

<!-- news -->
<h2 class="section-head" style="left:341px;top:518px">
  <svg width="43" height="43" viewBox="0 0 43 43"><circle cx="21" cy="22" r="19" fill="#1d3b55"/><path d="M4 18c8 2 14-6 22-2s10 10 15 8" stroke="#fff" stroke-width="3" fill="none"/><path d="M9 34c5-8 12-8 18-14" stroke="#fff" stroke-width="2.5" fill="none"/><path d="M32 4l9 3-5 7z" fill="#2aa0d8"/></svg>
  <span>News</span>
</h2>
<div class="news-item" style="top:590px">
  <div class="thumb" role="img" aria-label="Thumbnail of a DSLR camera"></div>
  <span class="title">Vestibulum ut purus in lorem.</span>
  <span class="lede">Lacus, et ultricies metus tempor. Integer ornare</span>
  <span class="date">August, 12</span>
</div>
<div class="news-item" style="top:672px">
  <div class="thumb" role="img" aria-label="Thumbnail of a DSLR camera"></div>
  <span class="title">Vestibulum ut purus in lorem.</span>
  <span class="lede">Lacus, et ultricies metus tempor. Integer ornare</span>
  <span class="date">August, 12</span>
</div>
<div class="news-item" style="top:754px">
  <div class="thumb" role="img" aria-label="Thumbnail of a DSLR camera"></div>
  <span class="title">Vestibulum ut purus in lorem.</span>
  <span class="lede">Lacus, et ultricies metus tempor. Integer ornare</span>
  <span class="date">August, 12</span>
</div>

<!-- black list -->
<h2 class="section-head" style="left:733px;top:520px">
  <svg width="38" height="40" viewBox="0 0 38 40"><path d="M10 2h16l8 8v28H10z" fill="none" stroke="#1d3b55" stroke-width="2.5"/><path d="M16 16h12M16 22h12M16 28h12" stroke="#1d3b55" stroke-width="2.5"/><path d="M1 26l8-8 8 8h-4v12H5V26z" fill="#2aa0d8"/></svg>
  <span>Black List</span>
</h2>
<ol class="black-list">
  <li><span class="name">1. Vivamus ut condimentum odio.</span><span class="note">Lacus, et ultricies metus tempor. Mauris lacinia tristique tellus.</span></li>
  <li><span class="name">2. Vivamus ut condimentum odio.</span><span class="note">Lacus, et ultricies metus tempor. Mauris lacinia tristique tellus.</span></li>
  <li><span class="name">3. Vivamus ut condimentum odio.</span><span class="note">Lacus, et ultricies metus tempor. Mauris lacinia tristique tellus.</span></li>
  <li><span class="name">4. Vivamus ut condimentum odio.</span><span class="note">Lacus, et ultricies metus tempor. Mauris lacinia tristique tellus.</span></li>
  <li><span class="name">5. Vivamus ut condimentum odio.</span><span class="note">Lacus, et ultricies metus tempor. Mauris lacinia tristique tellus.</span></li>
</ol>

<footer class="footer">Copyright © 2012 Lens Deal Scout</footer>

</body>
</html>
```